Romparoo - launching a new children's entertainment venue

Create a flyer (to be used online and offline) to promote a new business

Business name (tbc). Current considerations are:
# "Skylark for KIDS"
# "SK for KIDS"
# "SK Parties"

Concept
# A creative play space for young children
# To be used for either (i) birthday parties or (ii) general play area available for Mums/parents groups to hire

Facilities:
# General play space
# Basketball, soccer
# Ball pit
# Video games
# Movies

Room designed for 2-8 year olds in mind

Catering available:
# Party pies, sausage rolls and mini franks
# Potato chips
# Cordial and water
Note - cake not included
Kitchen facility available.

Party host

Use of parents retreat room

Packages (costs):
# 2 hour party with catering pack and host $220 (up to 10 children, $17.50 per child for additional children)
# 2 hour party - BYO and host $200 (up to 10 children, $15 per child for additional children)
# Casual hire (exclusive use of room and parents retreat) - $50 per hour

Note - we also require a new logo for this new business concept

Existing business is called Skylark Sports, a basketball training and development facility. The new business needs to be linked to Skylark Sports from a banding perspective although does require its own identity

Brand essence - fun, vibrant, colourful, engaging

Target Market(s)

Mums of children aged 2-8 years

Industry/Entity Type

Entertainment

Logo Text

Name "Skylark for KIDS" (although name is not 100% confirmed)

Font styles to use
Serif
Sans Serif

Requirements
Must have
• Must be vibrant, colourful and fun
• Get across sense of energy
Nice to have
• Some sort of link to existing business "Skylark Sports" logos are attached
• Although we have an open mind to a totally seperate brand

```html
<!DOCTYPE html>
<html lang="en">
<head>
<meta charset="utf-8">
<title>Skylark for KIDS – Flyer</title>
<link rel="stylesheet" href="https://fonts.googleapis.com/css2?family=Cabin:wght@400;600;700&family=Chewy&display=swap">
<style>
  :root {
    --blue: #1a73b8;
    --yellow: #f5ec2f;
    --red: #e8202a;
    --green: #8cc63f;
    --cyan: #29b1d6;
    --purple: #7b2a8c;
    --ink: #231f20;
    --white: #ffffff;
    --stage: #eef0f2;
  }
  * { box-sizing: border-box; margin: 0; padding: 0; }
  html, body { width: 1200px; height: 1200px; overflow: hidden; }
  body { background: var(--stage); font-family: "Cabin", sans-serif; color: var(--ink); position: relative; }

  .flyer {
    position: absolute; left: 172px; top: 47px;
    width: 855px; height: 1106px;
    background: var(--white); overflow: hidden;
    box-shadow: 0 6px 18px rgba(0,0,0,.18);
  }
  .top-strip { position: absolute; left: 0; top: 0; width: 100%; height: 16px; background: var(--yellow); }
  .tagline-band {
    position: absolute; left: 0; top: 16px; width: 100%; height: 70px; background: var(--blue);
    display: flex; align-items: center; justify-content: center; gap: 20px;
  }
  .tagline { font-family: "Chewy", "Cabin", sans-serif; color: var(--white); font-size: 32px; letter-spacing: .5px; white-space: nowrap; }
  .side-band-left { position: absolute; left: 0; top: 86px; width: 14px; bottom: 10px; background: var(--red); }
  .side-band-right { position: absolute; right: 0; top: 90px; width: 13px; height: 960px; background: var(--green); }
  .bottom-strip { position: absolute; left: 0; bottom: 0; width: 100%; height: 10px; background: var(--cyan); }

  .brand-name {
    position: absolute; left: 48px; top: 118px;
    font-family: "Cabin", sans-serif; font-weight: 700; color: var(--blue);
    font-size: 86px; line-height: .98;
  }

  .catering {
    position: absolute; left: 560px; top: 90px; width: 262px; height: 218px;
    background: var(--yellow);
    clip-path: polygon(0 0, 100% 0, 100% 80%, 0 100%);
    padding: 12px 18px;
  }
  .catering h2 { font-family: "Chewy", "Cabin", sans-serif; font-weight: 400; color: var(--purple); font-size: 29px; line-height: 1; margin-bottom: 6px; white-space: nowrap; }
  .catering ul { list-style: none; font-size: 17.5px; line-height: 23px; }
  .catering li::before { content: "• "; }
  .catering li .cont { padding-left: 10px; display: block; }
  .catering .note { font-size: 13px; line-height: 18px; padding-left: 10px; }

  .kids-photo {
    position: absolute; left: 302px; top: 290px; width: 540px; height: 816px;
    border-radius: 270px 270px 0 0;
    background: radial-gradient(ellipse at 50% 38%, #f3d3bf 0%, #eac3a8 25%, #5b9be0 52%, #e85a5e 74%, #fff1a8 100%);
  }

  .section-title { font-family: "Chewy", "Cabin", sans-serif; font-weight: 400; color: var(--blue); }
  .facilities { position: absolute; left: 40px; top: 358px; }
  .facilities h2 { font-size: 50px; line-height: 52px; margin-bottom: 6px; }
  .facilities ul { list-style: none; font-weight: 700; font-size: 23.5px; line-height: 32.5px; white-space: nowrap; }

  .gift-icon { position: absolute; left: 42px; top: 598px; width: 64px; height: 70px; background: #1a9a8a; border-radius: 3px; }
  .gift-icon-small { position: absolute; left: 112px; top: 632px; width: 30px; height: 36px; background: var(--red); border-radius: 2px; }

  .packages { position: absolute; left: 28px; top: 676px; width: 268px; }
  .packages h2 { font-size: 46px; line-height: 48px; margin-bottom: 6px; }
  .packages ul { list-style: none; font-size: 17px; line-height: 23.5px; white-space: nowrap; }
  .packages li { padding-left: 12px; position: relative; }
  .packages li::before { content: "•"; position: absolute; left: 2px; }
  .packages b { font-weight: 700; }

  .snap {
    position: absolute; border: 4px solid var(--yellow);
    box-shadow: 0 3px 6px rgba(0,0,0,.25);
  }
  .snap-court { left: 435px; top: 800px; width: 214px; height: 156px; transform: rotate(4deg); background: linear-gradient(180deg, #d8463c 0%, #f0b63a 40%, #3f7d35 60%, #2f6a2a 100%); }
  .snap-table { left: 632px; top: 802px; width: 198px; height: 148px; transform: rotate(-5deg); background: linear-gradient(180deg, #b5895a 0%, #c9a57c 45%, #3b7a34 75%, #2c5f2a 100%); }
  .snap-ballpit { left: 296px; top: 872px; width: 220px; height: 148px; transform: rotate(-4deg); background: linear-gradient(135deg, #3a4fb0, #e04a6a 50%, #f2c94c); }

  .call-box {
    position: absolute; left: 618px; top: 940px; width: 204px; height: 166px;
    background: var(--yellow); padding: 40px 0 0; text-align: center;
    color: var(--red); font-weight: 700;
  }
  .call-box .cta { font-size: 22px; line-height: 28px; }
  .call-box .phone { font-size: 24px; line-height: 30px; letter-spacing: .3px; }

  .web-band {
    position: absolute; left: 334px; top: 1026px; width: 540px; height: 50px;
    background: var(--red); transform: rotate(3deg); transform-origin: left center;
    display: flex; align-items: center; justify-content: flex-start; padding-left: 22px;
    color: var(--yellow); font-weight: 700; font-size: 25px; letter-spacing: .3px; white-space: nowrap;
  }

  .sparkle { position: absolute; }
</style>
</head>
<body>
<svg width="0" height="0" style="position:absolute">
  <defs>
    <symbol id="star" viewBox="0 0 24 24"><path d="M12 1l3.2 7 7.6.8-5.7 5.1 1.7 7.5L12 17.6 5.2 21.4l1.7-7.5L1.2 8.8 8.8 8z"/></symbol>
  </defs>
</svg>

<main class="flyer">
  <div class="top-strip"></div>
  <header class="tagline-band">
    <svg width="124" height="20"><use href="#star" x="0" width="20" height="20" fill="#f7941d"/><use href="#star" x="26" width="20" height="20" fill="#f49ac1"/><use href="#star" x="52" width="20" height="20" fill="#8cc63f"/><use href="#star" x="78" width="20" height="20" fill="#29b1d6"/><use href="#star" x="104" width="20" height="20" fill="#9ed8f0"/></svg>
    <p class="tagline">A creative play space for young children</p>
    <svg width="124" height="20"><use href="#star" x="0" width="20" height="20" fill="#9ed8f0"/><use href="#star" x="26" width="20" height="20" fill="#29b1d6"/><use href="#star" x="52" width="20" height="20" fill="#8cc63f"/><use href="#star" x="78" width="20" height="20" fill="#f49ac1"/><use href="#star" x="104" width="20" height="20" fill="#f7941d"/></svg>
  </header>
  <div class="side-band-left"></div>
  <div class="side-band-right"></div>

  <h1 class="brand-name">Skylark<br>for KIDS</h1>

  <section class="catering">
    <h2>Catering available:</h2>
    <ul>
      <li>Party pies, sausage rolls<span class="cont">and mini franks</span></li>
      <li>Potato chips</li>
      <li>Cordial and water</li>
    </ul>
    <p class="note">Note - cake not included<br>Kitchen facility available.</p>
  </section>

  <div class="kids-photo" role="img" aria-label="Photo of five smiling children in colourful t-shirts with arms raised and thumbs up"></div>

  <svg class="sparkle" style="left:299px;top:365px" width="22" height="22"><use href="#star" width="22" height="22" fill="#f49ac1"/></svg>
  <svg class="sparkle" style="left:346px;top:360px" width="24" height="24"><use href="#star" width="24" height="24" fill="#8cc63f"/></svg>
  <svg class="sparkle" style="left:389px;top:367px" width="34" height="34"><use href="#star" width="34" height="34" fill="#29b1d6"/></svg>
  <svg class="sparkle" style="left:428px;top:392px" width="48" height="48"><use href="#star" width="48" height="48" fill="#9ed8f0"/></svg>
  <svg class="sparkle" style="left:562px;top:380px" width="48" height="48"><use href="#star" width="48" height="48" fill="#f49ac1"/></svg>
  <svg class="sparkle" style="left:608px;top:342px" width="28" height="28"><use href="#star" width="28" height="28" fill="#8cc63f"/></svg>
  <svg class="sparkle" style="left:653px;top:315px" width="26" height="26"><use href="#star" width="26" height="26" fill="#29b1d6"/></svg>
  <svg class="sparkle" style="left:792px;top:422px" width="20" height="20"><use href="#star" width="20" height="20" fill="#f5ec2f"/></svg>
  <svg class="sparkle" style="left:756px;top:438px" width="28" height="28"><use href="#star" width="28" height="28" fill="#f49ac1"/></svg>
  <svg class="sparkle" style="left:714px;top:468px" width="48" height="48"><use href="#star" width="48" height="48" fill="#9ed8f0"/></svg>
  <svg class="sparkle" style="left:158px;top:562px" width="28" height="28"><use href="#star" width="28" height="28" fill="#f5ec2f"/></svg>
  <svg class="sparkle" style="left:785px;top:235px" width="22" height="22"><use href="#star" width="22" height="22" fill="#29b1d6"/></svg>

  <section class="facilities">
    <h2 class="section-title">Facilities:</h2>
    <ul>
      <li>- General play space</li>
      <li>- Basketball &amp; soccer</li>
      <li>- Ball pit</li>
      <li>- Video games</li>
      <li>- Movies</li>
    </ul>
  </section>

  <div class="gift-icon" role="img" aria-label="Gift box illustration"></div>
  <div class="gift-icon-small" role="img" aria-label="Small gift box illustration"></div>

  <section class="packages">
    <h2 class="section-title">Birthday<br>Packages:</h2>
    <ul>
      <li><b>2 hour party with<br>catering pack and host<br>$220</b> (up to 10 children,<br>$17.50 per child for<br>additional children)</li>
      <li><b>2 hour party - BYO and<br>host $200</b> (up to 10 children,<br>$15 per child for additional<br>children)</li>
      <li>Casual hire<br>(exclusive use of room and<br>parents retreat)<br>- $50 per hour</li>
    </ul>
  </section>

  <div class="snap snap-court" role="img" aria-label="Photo of children playing on an indoor turf court"></div>
  <div class="snap snap-table" role="img" aria-label="Photo of children at a party table"></div>
  <div class="snap snap-ballpit" role="img" aria-label="Photo of children playing in a ball pit"></div>

  <aside class="call-box">
    <p class="cta">CALL NOW!</p>
    <p class="phone">000-000-0000</p>
  </aside>
  <div class="web-band">WWW.SKYLARKKIDSPLAY.COM</div>

  <div class="bottom-strip"></div>
</main>
</body>
</html>
```